DWR Logistics Marketing flyer

Good morning, I run a trucking company and I will be needing help setting up a website logo and a marketing flyer or something like that talking about our services and what we can offer to potential new customers who need to ship their product. I need help getting this all together.

Target Market(s)

Transportation customers

Requirements
Must have
• should list our services and contact info
Nice to have
• the Logo on the top

```html
<!DOCTYPE html>
<html lang="en">
<head>
<meta charset="UTF-8">
<title>DWR Logistics – Flyer</title>
<link href="https://fonts.googleapis.com/css2?family=Oswald:wght@300;400;600;700&family=Roboto+Condensed:wght@700&display=swap" rel="stylesheet">
<style>
  :root{
    --bg-dark:#1a1a1a;
    --bg-mid:#2b2b2b;
    --silver-light:#f2f2f2;
    --silver-mid:#bdbdbd;
    --silver-dark:#7a7a7a;
    --text-light:#e6e6e6;
    --blue:#1f56a4;
    --blue-dark:#123a78;
    --red:#d7141b;
    --ink:#2a2a2a;
    --line:#9a9a9a;
  }
  *{box-sizing:border-box;margin:0;padding:0}
  html,body{width:781px;height:1200px;overflow:hidden;background:var(--bg-dark)}
  .flyer{
    position:relative;width:781px;height:1200px;overflow:hidden;
    background:radial-gradient(ellipse at 50% 35%, var(--bg-mid) 0%, var(--bg-dark) 70%);
    font-family:'Oswald',sans-serif;color:var(--text-light);
  }
  .brand{position:absolute;left:32px;top:56px;font-family:'Oswald',sans-serif;font-weight:600;
    font-size:44px;line-height:1.05;color:var(--silver-mid);letter-spacing:1px}
  .headline{position:absolute;right:46px;top:40px;text-align:right;font-weight:700;
    font-size:74px;line-height:1.17;letter-spacing:-0.5px;text-transform:uppercase;
    background:linear-gradient(180deg,var(--silver-light) 0%,var(--silver-mid) 45%,var(--silver-dark) 55%,var(--silver-light) 100%);
    -webkit-background-clip:text;background-clip:text;color:transparent}
  .services{position:absolute;left:26px;top:263px;width:726px;height:237px;
    border:1.5px solid var(--line);border-radius:14px;background:rgba(0,0,0,.18)}
  .services-label{position:absolute;left:284px;top:253px;width:210px;height:40px;
    background:linear-gradient(90deg,var(--blue-dark),var(--blue),var(--blue-dark));
    color:#d6e2f5;font-size:27px;font-weight:400;text-align:center;line-height:40px;letter-spacing:.5px}
  .service-list{position:absolute;top:312px;list-style:none;font-weight:300;font-size:17.5px;color:var(--text-light)}
  .service-list li{height:30px;display:flex;align-items:center;gap:9px;white-space:nowrap}
  .service-list.left{left:50px}
  .service-list.right{left:388px}
  .tick{width:15px;height:15px;flex:none}
  .truck-photo{position:absolute;left:130px;top:565px;width:651px;height:535px;
    background:radial-gradient(ellipse at 50% 50%, #9a9a9a 0%, #5c5c5c 35%, #2a2a2a 65%, transparent 80%)}
  .award{position:absolute;left:588px;top:488px;width:168px;height:168px;border-radius:50%;
    background:linear-gradient(135deg,#f5f5f5,#8a8a8a 50%,#e8e8e8);padding:9px}
  .award-inner{width:100%;height:100%;border-radius:50%;background:var(--red);
    display:flex;align-items:center;justify-content:center;text-align:center;
    font-weight:600;font-size:19px;line-height:1.2;color:#fff;transform:rotate(-14deg)}
  .contacts{position:absolute;left:24px;top:988px;width:283px;height:86px;border:1.5px solid #e0e0e0;
    border-radius:12px;overflow:hidden;background:var(--bg-dark)}
  .contacts-names{display:flex;background:#fff;height:38px;color:var(--ink);font-weight:600;font-size:14.5px;border-radius:0 0 12px 12px}
  .contacts-names span,.contacts-phones span{flex:1;display:flex;align-items:center;justify-content:center}
  .contacts-phones{display:flex;height:46px;font-weight:600;font-size:15px;color:#fff}
  .contacts-phones span+span{border-left:1.5px solid #fff;margin:9px 0}
  .footer{position:absolute;left:0;top:1110px;width:781px;height:90px}
  .footer-silver{position:absolute;inset:0;background:linear-gradient(90deg,#9a9a9a 40%,#e9e9e9 60%,#cfcfcf 80%,#f2f2f2)}
  .footer-blue{position:absolute;left:0;top:0;width:432px;height:90px;
    background:linear-gradient(90deg,var(--blue-dark),var(--blue));clip-path:polygon(0 0,395px 0,432px 90px,0 90px)}
  .email{position:absolute;left:30px;top:24px;font-family:'Roboto Condensed',sans-serif;font-weight:700;font-size:30px;color:#fff}
  .address{position:absolute;left:488px;top:17px;font-weight:300;font-size:19px;line-height:1.5;color:var(--ink)}
</style>
</head>
<body>
<main class="flyer">
  <div class="brand">DWR<br>Logistics</div>
  <h1 class="headline">Excellence<br>In Every Mile</h1>

  <section class="services" aria-label="Our services"></section>
  <div class="services-label">OUR SERVICES</div>
  <ul class="service-list left">
    <li><svg class="tick" viewBox="0 0 16 16"><rect x="1" y="3" width="11" height="11" fill="none" stroke="#e6e6e6" stroke-width="1.6"/><path d="M4 8l3 3 8-9" fill="none" stroke="#e6e6e6" stroke-width="2"/></svg>Handling of dry van, Reefer, flatbed, or tanker loads.</li>
    <li><svg class="tick" viewBox="0 0 16 16"><rect x="1" y="3" width="11" height="11" fill="none" stroke="#e6e6e6" stroke-width="1.6"/><path d="M4 8l3 3 8-9" fill="none" stroke="#e6e6e6" stroke-width="2"/></svg>Local and cross-country transportation services.</li>
    <li><svg class="tick" viewBox="0 0 16 16"><rect x="1" y="3" width="11" height="11" fill="none" stroke="#e6e6e6" stroke-width="1.6"/><path d="M4 8l3 3 8-9" fill="none" stroke="#e6e6e6" stroke-width="2"/></svg>Solo and team drivers available.</li>
    <li><svg class="tick" viewBox="0 0 16 16"><rect x="1" y="3" width="11" height="11" fill="none" stroke="#e6e6e6" stroke-width="1.6"/><path d="M4 8l3 3 8-9" fill="none" stroke="#e6e6e6" stroke-width="2"/></svg>Pride in customer service from pick up to delivery.</li>
    <li><svg class="tick" viewBox="0 0 16 16"><rect x="1" y="3" width="11" height="11" fill="none" stroke="#e6e6e6" stroke-width="1.6"/><path d="M4 8l3 3 8-9" fill="none" stroke="#e6e6e6" stroke-width="2"/></svg>Transportation of orange juice nationally.</li>
  </ul>
  <ul class="service-list right">
    <li><svg class="tick" viewBox="0 0 16 16"><rect x="1" y="3" width="11" height="11" fill="none" stroke="#e6e6e6" stroke-width="1.6"/><path d="M4 8l3 3 8-9" fill="none" stroke="#e6e6e6" stroke-width="2"/></svg>Handling of dry van, Reefer, flatbed, or tanker loads.</li>
    <li><svg class="tick" viewBox="0 0 16 16"><rect x="1" y="3" width="11" height="11" fill="none" stroke="#e6e6e6" stroke-width="1.6"/><path d="M4 8l3 3 8-9" fill="none" stroke="#e6e6e6" stroke-width="2"/></svg>Local and cross-country transportation services.</li>
    <li><svg class="tick" viewBox="0 0 16 16"><rect x="1" y="3" width="11" height="11" fill="none" stroke="#e6e6e6" stroke-width="1.6"/><path d="M4 8l3 3 8-9" fill="none" stroke="#e6e6e6" stroke-width="2"/></svg>Solo and team drivers available.</li>
    <li><svg class="tick" viewBox="0 0 16 16"><rect x="1" y="3" width="11" height="11" fill="none" stroke="#e6e6e6" stroke-width="1.6"/><path d="M4 8l3 3 8-9" fill="none" stroke="#e6e6e6" stroke-width="2"/></svg>Pride in customer service from pick up to delivery.</li>
    <li><svg class="tick" viewBox="0 0 16 16"><rect x="1" y="3" width="11" height="11" fill="none" stroke="#e6e6e6" stroke-width="1.6"/><path d="M4 8l3 3 8-9" fill="none" stroke="#e6e6e6" stroke-width="2"/></svg>Transportation of orange juice nationally.</li>
  </ul>

  <div class="truck-photo" role="img" aria-label="Photo of a white semi truck pulling a stainless steel tanker trailer"></div>

  <div class="award"><div class="award-inner">Winner of RTA<br>carrier excellence<br>award.</div></div>

  <div class="contacts">
    <div class="contacts-names"><span>CEO Mark Delaney</span><span>CEO Mark Delaney</span></div>
    <div class="contacts-phones"><span>555-204-7311</span><span>555-318-6402</span></div>
  </div>

  <footer class="footer">
    <div class="footer-silver"></div>
    <div class="footer-blue"></div>
    <div class="email">dwrlogisticsllc@mail.com</div>
    <div class="address">410 Oak Ct. Milltown, IN. 47100<br>www.yourwebsiteaddress.com</div>
  </footer>
</main>
</body>
</html>
```